Product label for herbal salves, lotions, soaps and tinctures

We need a very simple, clean and organic looking label that can be used for an ointment jar, a lotion bottle and a dropper bottle.
We have an existing logo (see attached). We like the colors white, olive green, gold and black. It needs to include product name as dominant and logo. It also needs to include an ingredient list, and usage statement. Include weight of product, distributed by, made in the USA, and NQB statement.
Example of what needs to be present:
Logo
Name: Calmwick Balm
Used for: For Muscle Aches, Arthritis, Tendonitis, Headaches
To Use: For muscle aches, arthritis and tendonitis, massage into affected area. For tension headache apply to neck, temples and forehead.
Store in a cool and dry place, away from direct heat and sunlight.
Weight of product: 1.75
DIST. BY: Brookmere Herbal
Made in the USA
This product is not intended to diagnose, treat, cure
or prevent any disease. Not regulated
by the NQB. Please consult your health care practitioner
before using product. Discontinue use if any adverse reaction occurs.
Ingredient list:
Wildcrafted Ingredients:
Ashwagandha Root, Peppermint Leaf, Hops Flowers, St. John’s Wort Herb, Arnica Flowers, Green Tea Leaf, Alfalfa Leaf, Dandelion Root, Burdock Root, Chickweed Herb, Chaparral Leaf, Yarrow Flowers, Boneset Herb, Moringa Leaf, Meadowsweet Herb, Nettle Leaf
Organic Ingredients:
Olive Oil, Aloe Leaf, Sweet Birch Bark, Helichrysum Flowers, Holy Basil Leaf, Borage Herb, Ginger Root, Angelica Root, White Willow Bark, Mustard Seed, Beeswax, Vitamin E, Essential Oils
Dimensions of Jar:
Circumference: 7 in.
Height: 1 in.

```html
<!DOCTYPE html>
<html lang="en">
<head>
<meta charset="utf-8">
<title>Calmwick Balm – Jar Label</title>
<link rel="stylesheet" href="https://fonts.googleapis.com/css2?family=Cinzel+Decorative:wght@700&family=Playfair+Display:wght@700&family=Open+Sans:wght@700;800&family=Poppins:ital,wght@0,400;0,600;1,400&display=swap">
<style>
  :root {
    --olive-light: #8aa838;
    --olive: #6f8f26;
    --olive-dark: #56731a;
    --gold: #c9a24a;
    --white: #ffffff;
    --ink: #2a2a2a;
    --ink-soft: #555555;
    --page: #f4f4f1;
  }
  * { box-sizing: border-box; margin: 0; padding: 0; }
  html, body { width: 1200px; height: 1200px; overflow: hidden; }
  body {
    background: var(--page);
    display: flex;
    align-items: center;
    justify-content: center;
  }
  .label {
    width: 1120px;
    height: 340px;
    display: flex;
    background: var(--white);
    box-shadow: 0 6px 24px rgba(0,0,0,0.12);
  }
  .front {
    width: 700px;
    display: flex;
    background: radial-gradient(ellipse at 30% 40%, var(--olive-light) 0%, var(--olive) 55%, var(--olive-dark) 100%);
    color: var(--white);
  }
  .brand-panel {
    width: 250px;
    display: flex;
    align-items: center;
    justify-content: center;
    gap: 10px;
    border-right: 3px dotted var(--gold);
    margin: 40px 0;
  }
  .brand-mark {
    width: 18px; height: 18px;
    border-radius: 50%;
    background: var(--gold);
    flex: none;
  }
  .brand-name {
    font-family: "Playfair Display", serif;
    font-weight: 700;
    font-size: 30px;
    line-height: 1.1;
    color: var(--white);
  }
  .name-panel {
    flex: 1;
    padding: 60px 30px 0 36px;
  }
  .title-row { display: flex; align-items: flex-end; gap: 12px; }
  .product-name {
    font-family: "Cinzel Decorative", serif;
    font-weight: 700;
    font-size: 50px;
    line-height: 1.05;
    color: var(--white);
  }
  .sprig {
    width: 80px; height: 56px;
    background: linear-gradient(135deg, rgba(255,255,255,0.35), rgba(201,162,74,0.35));
    border-radius: 4px;
    margin-bottom: 6px;
  }
  .uses {
    margin-top: 26px;
    font-family: "Open Sans", sans-serif;
    font-weight: 800;
    font-size: 19px;
    line-height: 1.35;
    text-transform: uppercase;
  }
  .back {
    flex: 1;
    display: flex;
    padding: 26px 20px 20px 24px;
    gap: 18px;
    font-family: "Poppins", sans-serif;
    color: var(--ink);
  }
  .ingredients { flex: 1; font-size: 10.5px; line-height: 1.5; }
  .ingredients strong { font-weight: 600; }
  .ingredients p + p { margin-top: 8px; }
  .ingredients em { color: var(--ink-soft); }
  .info {
    width: 118px;
    border-left: 1px solid var(--gold);
    padding-left: 10px;
    font-size: 7.5px;
    line-height: 1.45;
    color: var(--ink-soft);
  }
  .info .weight { font-size: 10px; font-weight: 600; color: var(--ink); margin-bottom: 6px; }
  .info p + p { margin-top: 6px; }
</style>
</head>
<body>
  <div class="label">
    <div class="front">
      <div class="brand-panel">
        <span class="brand-mark"></span>
        <span class="brand-name">Brookmere Herbal</span>
      </div>
      <div class="name-panel">
        <div class="title-row">
          <h1 class="product-name">Calmwick<br>Balm</h1>
          <div class="sprig" role="img" aria-label="Faint olive sprig illustration"></div>
        </div>
        <p class="uses">For muscle aches, arthritis,<br>tendonitis, headaches</p>
      </div>
    </div>
    <div class="back">
      <div class="ingredients">
        <p><strong>Wildcrafted Ingredients:</strong> Ashwagandha Root, Peppermint Leaf, Hops Flowers, St. John’s Wort Herb, Arnica Flowers, Green Tea Leaf, Alfalfa Leaf, Dandelion Root, Burdock Root, Chickweed Herb, Chaparral Leaf, Yarrow Flowers, Boneset Herb, Moringa Leaf, Meadowsweet Herb, Nettle Leaf <strong>Organic Ingredients:</strong> Olive Oil, Aloe Leaf, Sweet Birch Bark, Helichrysum Flowers, Holy Basil Leaf, Borage Herb, Ginger Root, Angelica Root, White Willow Bark, Mustard Seed, Beeswax, Vitamin E, Essential Oils</p>
        <p><strong>To Use:</strong> For muscle aches, arthritis and tendonitis, massage into affected area. For tension headache apply to neck, temples and forehead.</p>
        <p><em>Store in a cool and dry place, away from direct heat and sunlight.</em></p>
      </div>
      <div class="info">
        <p class="weight">Net Wt. 1.75 oz</p>
        <p>DIST. BY: Brookmere Herbal</p>
        <p>Made in the USA</p>
        <p>This product is not intended to diagnose, treat, cure or prevent any disease. Not regulated by the NQB. Please consult your health care practitioner before using product. Discontinue use if any adverse reaction occurs.</p>
      </div>
    </div>
  </div>
</body>
</html>
```